Refresh of Business Card Design

Want to refresh the business card design with the new logo while adhering to style guide as attached. Would like to match feel of website www.durmackvinex.com

```html
<!DOCTYPE html>
<html lang="en">
<head>
<meta charset="utf-8">
<title>Durmack Vinex – Business Card</title>
<link href="https://fonts.googleapis.com/css2?family=Montserrat:wght@700&family=Open+Sans:wght@400;600&display=swap" rel="stylesheet">
<style>
  :root {
    --bg: #1d1d1f;
    --card: #0b0b0c;
    --red: #d8262f;
    --red-dark: #b81e26;
    --white: #f4f4f4;
    --grey: #8a8a8a;
    --silver-light: #f2f2f2;
    --silver-dark: #a9a9a9;
    --ink: #1a1a1a;
  }
  html, body {
    margin: 0;
    width: 1200px;
    height: 900px;
    overflow: hidden;
    background: var(--bg);
    font-family: "Open Sans", Arial, sans-serif;
  }
  .canvas {
    position: relative;
    width: 1200px;
    height: 900px;
  }
  .card {
    position: absolute;
    left: 270px;
    width: 660px;
    height: 377px;
    border-radius: 22px;
    overflow: hidden;
    background: var(--card);
  }
  .card--front { top: 40px; }
  .card--back { top: 483px; }
  .card svg { display: block; width: 660px; height: 377px; }
  .brand-name {
    font-family: "Open Sans", Arial, sans-serif;
    font-weight: 600;
    fill: var(--white);
    letter-spacing: 2px;
  }
  .person-name {
    font-family: "Montserrat", Arial, sans-serif;
    font-weight: 700;
    font-size: 26px;
    fill: var(--red);
  }
  .person-role { font-size: 16px; fill: var(--white); }
  .contact { font-size: 14.5px; fill: var(--white); }
  .url-front { font-size: 17px; fill: var(--white); letter-spacing: 2px; }
  .url-back { font-size: 15px; fill: var(--ink); letter-spacing: 2px; }
</style>
</head>
<body>
<main class="canvas">

  <section class="card card--front" aria-label="Card front">
    <svg viewBox="0 0 660 377" xmlns="http://www.w3.org/2000/svg">
      <defs>
        <linearGradient id="redBand" x1="0" y1="1" x2="1" y2="0">
          <stop offset="0" stop-color="var(--red-dark)"/>
          <stop offset="1" stop-color="var(--red)"/>
        </linearGradient>
        <path id="frontUrlCurve" d="M120,372 C260,336 440,312 640,300"/>
      </defs>

      <g class="brand-lockup">
        <circle cx="62" cy="196" r="14" fill="var(--red)"/>
        <text class="brand-name" x="86" y="203" font-size="20">DURMACK VINEX</text>
      </g>

      <line class="divider" x1="320" y1="72" x2="320" y2="238" stroke="var(--grey)" stroke-width="0.8"/>

      <g class="contact-block">
        <text class="person-name" x="340" y="100">ROWAN PELLEY</text>
        <text class="person-role" x="342" y="122">Sales</text>

        <g class="icon-phone" transform="translate(342,148)" fill="var(--red)">
          <path d="M3,1 L6,1 L7.5,5 L5.5,6.5 C6.5,8.5 8,10 10,11 L11.5,9 L15,10.5 L15,13.5 C15,14.5 14,15 13,15 C6.5,14.5 1.5,9.5 1,3 C1,2 1.8,1 3,1 Z"/>
        </g>
        <text class="contact" x="364" y="161">555.014.2290</text>

        <g class="icon-mail" transform="translate(342,172)">
          <rect x="0" y="1" width="15" height="11" rx="1" fill="var(--red)"/>
          <path d="M0.5,1.5 L7.5,7.5 L14.5,1.5" fill="none" stroke="var(--card)" stroke-width="1.2"/>
        </g>
        <text class="contact" x="364" y="184">rpelley@durmackvinex.com</text>

        <text class="contact" x="342" y="214">P.O.Box 40218 Harlow, TX 70041</text>
        <text class="contact" x="342" y="235">52 Quarry Ln Ashby, Texas 70288</text>
      </g>

      <path class="accent-band" d="M0,377 C140,318 360,278 660,266 L660,377 Z" fill="url(#redBand)"/>
      <text class="url-front">
        <textPath href="#frontUrlCurve" startOffset="50%" text-anchor="middle">www.durmackvinex.com</textPath>
      </text>
    </svg>
  </section>

  <section class="card card--back" aria-label="Card back">
    <svg viewBox="0 0 660 377" xmlns="http://www.w3.org/2000/svg">
      <defs>
        <linearGradient id="silverBand" x1="0" y1="1" x2="1" y2="0">
          <stop offset="0" stop-color="var(--silver-dark)"/>
          <stop offset="0.55" stop-color="var(--silver-light)"/>
          <stop offset="1" stop-color="var(--silver-dark)"/>
        </linearGradient>
        <path id="backUrlCurve" d="M200,342 C340,292 500,230 640,198"/>
      </defs>

      <g class="brand-lockup">
        <circle cx="206" cy="150" r="16" fill="var(--red)"/>
        <text class="brand-name" x="234" y="158" font-size="23">DURMACK VINEX</text>
      </g>

      <path class="accent-band" d="M0,377 L0,372 C220,320 450,210 660,172 L660,377 Z" fill="url(#silverBand)"/>
      <path d="M0,377 C220,345 450,250 660,215 L660,377 Z" fill="var(--card)"/>
      <text class="url-back">
        <textPath href="#backUrlCurve" startOffset="55%" text-anchor="middle">www.durmackvinex.com</textPath>
      </text>
    </svg>
  </section>

</main>
</body>
</html>
```